K7 Electrical Services Ltd Web design

I require a web site for my new electrical contracting company. We are customer service orientated. Offering high value electrical installations, design and maintenance. Focused on custom residential and commercial upgrading. Lighting design and application are paramount in our company's services. Industry leading product use and integration are always on the forefront with our customer client services. As well as energy efficiency.

Target Market(s)

Homebuilders, General Contractors, Property management companies, clients, individuals,

Industry/Entity Type

Electric Company

Coding

Coded - Design and coding required

Number of Pages Required

3 page

Requirements
Must have
• Classic, modern, edgy but not trendy . Appeals to the masse.
• 3 page
• home page
• about page
• gallery page
• ability to contact from the webiste
Nice to have
• open to all types of designs that are relative to the construction industry.
• Black, Grey, metallic ice blue and deep purple colours from the logo.
Should not have
• anything cheesy with cartoon light bulb images.

```html
<!DOCTYPE html>
<html lang="en">
<head>
<meta charset="utf-8">
<title>K7 Electrical Services Ltd</title>
<link href="https://fonts.googleapis.com/css2?family=Montserrat:wght@400;500;600;700&family=Open+Sans:wght@400;600;700&display=swap" rel="stylesheet">
<style>
:root{
  --purple:#7b2fb5;
  --purple-deep:#5a2a8c;
  --dark:#2b2d3a;
  --charcoal:#333333;
  --footer:#2e2e2e;
  --red:#e01e1e;
  --orange:#f26a1b;
  --text:#555a60;
  --muted:#8a8f96;
  --light:#f2f3f5;
  --white:#ffffff;
}
*{box-sizing:border-box;margin:0;padding:0}
html,body{width:1200px;height:3442px;overflow:hidden}
body{position:relative;background:var(--white);font-family:"Open Sans",Arial,sans-serif;color:var(--text)}
.abs{position:absolute}
.heading{font-family:"Montserrat",Arial,sans-serif}
.photo{position:absolute}

/* header */
.top-strip{left:0;top:0;width:1200px;height:18px;background:#5f5f63}
.social{display:flex;gap:8px}
.social span{width:28px;height:28px;border-radius:50%;background:#222}
.brand{left:0;width:1200px;top:40px;text-align:center;font-family:"Montserrat",sans-serif;font-weight:700;font-size:30px;color:var(--purple-deep);letter-spacing:1px}
.header-phone{right:154px;top:60px;text-align:right}
.header-phone .num{font-size:24px;color:var(--charcoal);display:flex;align-items:center;gap:6px;justify-content:flex-end}
.header-phone .tag{font-size:13px;font-style:italic;color:#222;margin-top:2px}

.nav{left:122px;top:130px;width:956px;height:47px;background:var(--purple);z-index:2}
.nav a{position:absolute;top:0;line-height:47px;transform:translateX(-50%);font-family:"Montserrat",sans-serif;font-weight:600;font-size:13px;color:var(--white);text-decoration:none}
.nav .search{position:absolute;left:908px;top:13px;width:26px;height:22px;background:#2d8ce8}

/* hero */
.hero{left:0;top:156px;width:1200px;height:562px;background:linear-gradient(180deg,#aebfcf 0%,#d9e2ea 45%,#c9d3dc 100%)}
.hero-line{left:122px;font-family:"Montserrat",sans-serif;font-weight:500;font-size:34px;color:var(--white);padding:0 18px;height:54px;line-height:54px}
.hero-line.one{top:344px;background:rgba(30,30,34,.85)}
.hero-line.two{top:399px;background:var(--purple)}

/* welcome */
.welcome-title{left:0;width:1244px;top:784px;text-align:center;font-size:33px;font-weight:500;color:#222}
.welcome-sub{left:0;width:1244px;top:832px;text-align:center;font-size:13px;color:var(--muted)}
.welcome-copy{left:645px;top:884px;width:390px;font-size:12px;line-height:20px;color:var(--muted)}
.ticks{list-style:none}
.ticks li{display:flex;align-items:center;gap:10px;font-size:12px;height:27px}
.btn{display:inline-block;font-family:"Montserrat",sans-serif;font-size:12px;text-align:center;border-radius:22px}
.btn-red{left:645px;top:1104px;width:147px;height:41px;line-height:41px;background:var(--red);color:var(--white);font-weight:500}

/* who we are */
.who{left:0;top:1228px;width:634px;height:436px;background:var(--dark)}
.who-title{left:71px;top:1316px;font-size:30px;font-weight:500;color:var(--white)}
.who-sub{left:71px;top:1360px;font-size:13px;color:#e8e8ee;font-weight:600}
.who-copy{left:71px;top:1396px;width:500px;font-size:12px;line-height:21px;color:#d2d3da}
.who-list{list-style:none;font-size:12px;color:#e6e6ea}
.who-list li{height:28px;padding-left:24px;position:relative}
.who-list li::before{content:"";position:absolute;left:0;top:6px;width:6px;height:6px;border-radius:50%;background:var(--purple)}
.play{left:866px;top:1382px;width:72px;height:72px}

/* gallery */
.section-title{font-family:"Montserrat",sans-serif;font-weight:500;font-size:21px;color:#222;letter-spacing:.5px}
.tile{position:absolute;width:289px;height:186px;overflow:hidden}
.tile .label{position:absolute;left:0;right:0;bottom:12px;text-align:center;font-family:"Montserrat",sans-serif;font-weight:700;font-size:13px;color:var(--white);letter-spacing:.4px}
.tile.feature{background:#9b4fd1;color:var(--white);text-align:center;padding:52px 40px 0}
.tile.feature h3{font-family:"Montserrat",sans-serif;font-size:14px;font-weight:700;margin-bottom:12px}
.tile.feature p{font-size:12px;line-height:19px;color:#efe3fa}

/* cta */
.cta{left:0;top:2322px;width:1200px;height:202px;background:var(--dark)}
.cta-title{left:0;width:1200px;top:2358px;text-align:center;font-size:29px;color:var(--white)}
.cta-title b{font-weight:700}
.cta-sub{left:0;width:1200px;top:2398px;text-align:center;font-size:17px;color:#d8d8e0}
.btn-orange{left:429px;top:2446px;width:129px;height:37px;line-height:37px;border-radius:2px;background:var(--orange);color:var(--white);font-weight:600}
.btn-white{left:581px;top:2446px;width:183px;height:37px;line-height:37px;border-radius:2px;background:var(--white);color:#222;font-weight:600}

/* blogs */
.blogs-bg{left:0;top:2524px;width:1200px;height:556px;background:var(--light)}
.sub-head{font-family:"Montserrat",sans-serif;font-weight:700;font-size:20px;color:#222;letter-spacing:.5px}
.post{position:absolute;left:142px;width:443px;height:161px;background:var(--white)}
.post .thumb{position:absolute;left:0;top:0;width:159px;height:161px}
.post .date{position:absolute;left:0;bottom:0;width:40px;height:40px;background:var(--purple);color:var(--white);text-align:center;font-weight:700;font-size:16px;line-height:20px;padding-top:2px}
.post .date small{display:block;font-size:9px;font-weight:400;line-height:10px}
.post h4{position:absolute;left:180px;top:14px;font-family:"Montserrat",sans-serif;font-size:12px;font-weight:700;color:#222}
.post p{position:absolute;left:180px;top:44px;width:245px;font-size:11px;line-height:19px;color:var(--muted)}
.post .meta{position:absolute;left:180px;top:128px;font-size:10px;color:var(--muted);border-top:1px solid #e5e5e5;padding-top:6px;width:245px}

.avatar{left:693px;top:2662px;width:92px;height:92px;border-radius:50%;background:linear-gradient(160deg,#d7dce3,#8d96a3)}
.quote-name{left:822px;top:2668px;font-family:"Montserrat",sans-serif;font-weight:600;font-size:14px;color:#222}
.quote-role{left:822px;top:2692px;font-size:11px;color:var(--muted)}
.stars{left:822px;top:2722px;display:flex;gap:5px}
.quote{left:691px;top:2782px;width:385px;font-size:11px;line-height:19px;color:var(--muted)}
.signature{left:691px;top:2876px;width:130px;height:50px;background:linear-gradient(90deg,#e6e7ea,#d9dadd)}
.dots{left:855px;top:2971px;display:flex;gap:8px}
.dots span{width:9px;height:9px;border-radius:50%}
.side-tab{left:1188px;top:2985px;width:12px;height:30px;background:#2d8ce8}

/* footer */
.promo{left:0;top:3080px;width:1200px;height:46px;background:var(--purple);color:var(--white);font-family:"Montserrat",sans-serif;font-size:20px;font-weight:500}
.promo span{position:absolute;top:0;line-height:46px}
.footer{left:0;top:3126px;width:1200px;height:316px;background:var(--footer)}
.footer-brand{left:142px;top:3206px;font-family:"Montserrat",sans-serif;font-weight:700;font-size:24px;color:var(--white);letter-spacing:.5px}
.copyright{left:142px;top:3284px;font-size:12px;color:#b8b8bc}
.footer-social{left:154px;top:3317px;display:flex;gap:6px}
.footer-social span{width:32px;height:32px;border-radius:50%;background:#707074}
.contact{left:390px;font-size:12px;color:#e4e4e8}
.contact b{font-weight:400;color:#b8b8bc}
.map{left:700px;top:3179px;width:367px;height:177px;background:linear-gradient(135deg,#eef0ec,#dfe3dd)}
</style>
</head>
<body>

<!-- header -->
<div class="abs top-strip"></div>
<div class="abs social" style="left:181px;top:70px"><span></span><span></span><span></span><span></span></div>
<div class="abs brand">K7 Electrical</div>
<div class="abs header-phone">
  <div class="num">
    <svg width="16" height="16" viewBox="0 0 24 24"><path fill="#7b2fb5" d="M6.6 10.8a15 15 0 0 0 6.6 6.6l2.2-2.2c.3-.3.7-.4 1-.2 1.1.4 2.3.6 3.6.6.6 0 1 .4 1 1V20c0 .6-.4 1-1 1A17 17 0 0 1 3 4c0-.6.4-1 1-1h3.5c.6 0 1 .4 1 1 0 1.3.2 2.5.6 3.6.1.3 0 .7-.2 1z"/></svg>
    1 (800) 555-0142
  </div>
  <div class="tag">Call us now. Resistance is futile!</div>
</div>

<nav class="abs nav">
  <a href="#" style="left:41px">HOME</a>
  <a href="#" style="left:155px">SERVICES</a>
  <a href="#" style="left:284px">ELECTRICITY</a>
  <a href="#" style="left:419px">PROJECTS</a>
  <a href="#" style="left:541px">GALLERY</a>
  <a href="#" style="left:663px">ABOUT US</a>
  <a href="#" style="left:798px">CONTACT US</a>
  <span class="search"></span>
</nav>

<!-- hero -->
<div class="photo hero" role="img" aria-label="Bright warehouse interior with a yellow forklift under a steel roof"></div>
<div class="abs hero-line one heading">Commercial Upgrading</div>
<div class="abs hero-line two heading">Electrical Services</div>

<!-- welcome -->
<div class="photo" style="left:142px;top:722px;width:14px;height:280px;background:linear-gradient(180deg,#d8cfc4,#b9ab9a)" role="img" aria-label="Hanging pendant lamp on a cord"></div>
<h1 class="abs welcome-title heading">Welcome to K7 Electrical</h1>
<div class="abs welcome-sub">Lorem ipsum dolor sit amet consectetur adipisicing elit sed do eiusm tempor</div>
<div class="photo" style="left:271px;top:868px;width:245px;height:295px;background:linear-gradient(180deg,#c9ced8,#3f51a8 55%,#2d3a80)" role="img" aria-label="Electrician in blue overalls carrying a coil of cable"></div>
<div class="abs welcome-copy">
  <p>Excepteur sint occaecat cupidatat non proident, sunt in culpa qui officia deserunt mollit anim id est laborum. Sed ut perspiciatis unde omnis natus error sit voluptatem accusantium doloremque laudantium totam rem aperiam eaque ipsa quae ab illo inventore veritatis et quasi archite beatae vitae dicta sunt explicabo.</p>
  <ul class="ticks" style="margin-top:14px">
    <li><svg width="10" height="10" viewBox="0 0 10 10"><path d="M1 5l3 3 5-7" stroke="#e01e1e" stroke-width="2" fill="none"/></svg>Morbi fermentum felis nec</li>
    <li><svg width="10" height="10" viewBox="0 0 10 10"><path d="M1 5l3 3 5-7" stroke="#e01e1e" stroke-width="2" fill="none"/></svg>Morbi fermentum felis nec gravida tempus</li>
    <li><svg width="10" height="10" viewBox="0 0 10 10"><path d="M1 5l3 3 5-7" stroke="#e01e1e" stroke-width="2" fill="none"/></svg>Morbi fermentum felis nec gravida</li>
  </ul>
</div>
<a class="abs btn btn-red">CONTACT NOW</a>

<!-- who we are -->
<div class="abs who"></div>
<h2 class="abs who-title heading">Who We Are</h2>
<div class="abs who-sub">Lorem ipsum dolor sit amet consectetur adipisicing elit sed do eiusm tempor</div>
<p class="abs who-copy">Excepteur sint occaecat cupidatat non proident, sunt in culpa qui officia deserunt mollit anim id est laborum. Sed ut perspiciatis unde omnis iste natus error sit voluptatem accusantium doloremque laudantium totam rem aperiam eaque ipsa quae ab illo inventore veritatis et quasi architecto.</p>
<ul class="abs who-list" style="left:74px;top:1500px">
  <li>Morbi fermentum felis nec</li><li>Aenean pulvinar nunc eu.</li><li>Mollis pulvinar maximus.</li>
</ul>
<ul class="abs who-list" style="left:288px;top:1500px">
  <li>Fusce eleifend massa eget.</li><li>Rutrum nibh ut purus vestibulum.</li><li>Justo id libero tempor malesua.</li>
</ul>
<div class="photo" style="left:634px;top:1228px;width:566px;height:416px;background:linear-gradient(135deg,#8aa0b8,#35435a 60%,#1f2838)" role="img" aria-label="Electrician in a hard hat working on overhead wiring"></div>
<svg class="abs play" viewBox="0 0 72 72"><circle cx="36" cy="36" r="36" fill="#7b2fb5"/><path d="M28 22l22 14-22 14z" fill="#fff"/></svg>

<!-- gallery -->
<h2 class="abs section-title" style="left:0;width:1200px;text-align:center;top:1766px">OUR GALLERY</h2>
<div class="tile" style="left:142px;top:1836px;background:linear-gradient(160deg,#6d7f96,#2f3a4c)" role="img" aria-label="Technicians testing a switchboard"><div class="label">TESTING &amp; INSPECTION</div></div>
<div class="tile feature" style="left:454px;top:1836px"><h3>DOMESTIC PROJECT</h3><p>Duis aute irure dolor in reprehenderit in voluptate velit esse cillum dolore eu fugiat nulla pariatur.</p></div>
<div class="tile" style="left:766px;top:1836px;background:linear-gradient(160deg,#e4e2df,#7d8595)" role="img" aria-label="Electrician fitting a wall socket"><div class="label">DOMESTIC PROJECT</div></div>
<div class="tile" style="left:142px;top:2047px;background:linear-gradient(160deg,#7fa6d0,#5a4a40)" role="img" aria-label="Worker with large cable reels"><div class="label">COMMERCIAL PROJECT</div></div>
<div class="tile" style="left:454px;top:2047px;background:linear-gradient(160deg,#a8a79f,#3c4354)" role="img" aria-label="Electrician wiring a panel"><div class="label">OFFICIAL PROJECT</div></div>
<div class="tile" style="left:766px;top:2047px;background:linear-gradient(160deg,#8896a8,#2c3647)" role="img" aria-label="Two technicians servicing a control cabinet"><div class="label">REPAIRING &amp; MAINTENANCE</div></div>

<!-- call to action -->
<div class="abs cta"></div>
<h2 class="abs cta-title heading" style="font-weight:400">Do you need help with <b>electrical maintenance?</b></h2>
<p class="abs cta-sub">Contact us – our technicians are ready to help you solve that issue.</p>
<a class="abs btn btn-orange">&#9990; Give Us A Call</a>
<a class="abs btn btn-white"><span style="color:#f26a1b">&#9889;</span> Request A Free Estimate</a>

<!-- blogs & testimonials -->
<div class="abs blogs-bg"></div>
<h3 class="abs sub-head" style="left:142px;top:2578px">LATEST BLOGS</h3>
<h3 class="abs sub-head" style="left:691px;top:2578px">TESTIMONIALS</h3>

<article class="post" style="top:2657px">
  <div class="thumb" role="img" aria-label="Electrician working at a wall box" style="background:linear-gradient(160deg,#e9e6e0,#c3a27a)"></div>
  <div class="date">9<small>Aug</small></div>
  <h4>THIS IS JUST A POST</h4>
  <p>Sed ut perspiciatis unde omnis iste natus error sit voluptatem accusa nt ium dolore mque laudantium totam rem</p>
  <div class="meta">By: Admin &nbsp;|&nbsp; Read more</div>
</article>
<article class="post" style="top:2843px">
  <div class="thumb" role="img" aria-label="White pendant lamp" style="background:linear-gradient(180deg,#d4b699,#f4f2ef)"></div>
  <div class="date">9<small>Aug</small></div>
  <h4>A SAMPLE BLOG POST</h4>
  <p>Sed ut perspiciatis unde omnis iste natus error sit voluptatem accusa nt ium dolore mque laudantium totam rem</p>
  <div class="meta">By: Admin &nbsp;|&nbsp; Read more</div>
</article>

<div class="abs avatar" role="img" aria-label="Client portrait"></div>
<div class="abs quote-name">Electrician is Great Firm</div>
<div class="abs quote-role">Daniel Reeves (CEO &amp; Founder)</div>
<div class="abs stars">
  <svg width="60" height="11" viewBox="0 0 60 11"><g fill="#333"><circle cx="5" cy="5.5" r="3.5"/><circle cx="17" cy="5.5" r="3.5"/><circle cx="29" cy="5.5" r="3.5"/><circle cx="41" cy="5.5" r="3.5"/><circle cx="53" cy="5.5" r="3.5"/></g></svg>
</div>
<p class="abs quote">Neque porro quisquam est, qui dolorem ipsum quia dolor sit amet, consectetur, adipis civelit sed quia non qui dolorem ipsum quia dolor sit amet, consectetur, adipis civelit sed quia numquam eius modi. Neque porro quisquam est, qui dolorem ipsum</p>
<div class="abs signature" role="img" aria-label="Handwritten signature"></div>
<div class="abs dots"><span style="background:#f26a1b"></span><span style="background:#7b2fb5"></span></div>
<div class="abs side-tab"></div>

<!-- footer -->
<div class="abs promo">
  <span style="left:158px">24/Hour Emergency Service</span>
  <span style="left:530px">•&nbsp;&nbsp; Free Consultations</span>
  <span style="left:832px">•&nbsp;&nbsp; 1 (800) 555-0142</span>
</div>
<div class="abs footer"></div>
<div class="abs footer-brand">K7 Electrical</div>
<div class="abs copyright">© 2016 Electrical Services.</div>
<div class="abs footer-social"><span></span><span></span><span></span></div>
<div class="abs contact" style="top:3195px"><b>Phone:</b> &nbsp;1 (800) 555-0142</div>
<div class="abs contact" style="top:3224px;width:300px;line-height:20px"><b>Address:</b> 1200 Harbor Point Road Lakeview, VA, 20100</div>
<div class="abs contact" style="top:3272px"><b>Email:</b> &nbsp;&nbsp;info@k7electrical.example</div>
<div class="abs contact" style="top:3302px">Mon-Fri 08:00 AM - 05:00 PM, Sat-Sun</div>
<div class="abs map" role="img" aria-label="Street map showing the office location"></div>

</body>
</html>
```